Book Cover - Goals

Create book cover for book
Title: Summit Drive
Subtitle: Push Past Your Limits, Find Strength Within Yourself

See the uploaded 1st version -- I want to see different concepts -- definitely want use white space and keep a blue color similiar if not the same as the one seen in that other version and see my notes/feedback.

:

Target Market(s)

Women + Men - 35-60
Self Help + Health

Industry/Entity Type

Health And Wellness

Font styles to use
Sans Serif

Colors
0692cd
34a7d7
85cae6
cee9f5

Requirements
Must have
• Picture of father and I that can be found here:(https://files.cloudvault-share.net/folders/7K9QxRm2_41PlVnwTbZuLeHsCq3)
• and I uploaded one too (I'd like to see it with our shirts on and off)
Nice to have
• Want it to be clean
• More gender neutral -- not overly masculine or femine
• I really like these book covers - so something similair woudl be great"
• Steady Steps: The 9-Week Meal Rhythm Method
• The Quiet Harvest Plan : Retune Your Habits for Gentle Fat Burning, Steady Vigor and Lasting Stamina
• Walk Far, Feel Light for Years

```html
<!DOCTYPE html>
<html lang="en">
<head>
<meta charset="utf-8">
<title>Summit Drive – Book Cover</title>
<link rel="stylesheet" href="https://fonts.googleapis.com/css2?family=Comfortaa:wght@700&family=Arimo:wght@700&display=swap">
<style>
  :root {
    --blue-deep: #0692cd;
    --blue-mid: #34a7d7;
    --blue-soft: #85cae6;
    --blue-pale: #cee9f5;
    --blue-bright: #5cb8e0;
    --blue-ink: #0b5f93;
    --blue-dusk: #1f7fb8;
    --blue-ice: #a6d8ee;
    --page: #d8eef8;
    --white: #ffffff;
    --tagline: #2a9fd6;
  }
  html, body {
    margin: 0;
    padding: 0;
    width: 848px;
    height: 1200px;
    overflow: hidden;
    background: var(--page);
  }
  .cover {
    position: relative;
    width: 848px;
    height: 1200px;
    overflow: hidden;
    background: var(--page);
  }
  .facets {
    position: absolute;
    left: 0;
    top: 0;
    width: 848px;
    height: 1200px;
  }
  .portrait {
    position: absolute;
    left: 14px;
    top: 413px;
    width: 596px;
    height: 690px;
    background: linear-gradient(180deg, #d8eef8 0%, #e3b79a 10%, #d9a584 45%, #c99274 62%, #4d8dc0 78%, #c95a48 92%, #c95a48 100%);
    border-radius: 40px 40px 0 0;
    opacity: 0.85;
  }
  .title {
    position: absolute;
    left: 0;
    top: 118px;
    width: 848px;
    margin: 0;
    text-align: center;
    font-family: "Comfortaa", sans-serif;
    font-weight: 700;
    font-size: 142px;
    line-height: 150px;
    letter-spacing: 1px;
    color: var(--white);
    text-shadow: 0 0 10px rgba(120, 200, 240, 0.95), 0 0 22px rgba(52, 167, 215, 0.7);
  }
  .tagline {
    position: absolute;
    left: 624px;
    top: 446px;
    width: 210px;
    margin: 0;
    font-family: "Arimo", sans-serif;
    font-weight: 700;
    font-size: 25px;
    line-height: 38px;
    color: var(--tagline);
  }
  .authors {
    position: absolute;
    left: 11px;
    top: 1082px;
    margin: 0;
    font-family: "Comfortaa", sans-serif;
    font-weight: 700;
    font-size: 50px;
    line-height: 60px;
    color: var(--white);
  }
  .team {
    position: absolute;
    left: 12px;
    top: 1150px;
    margin: 0;
    font-family: "Arimo", sans-serif;
    font-weight: 700;
    font-size: 27px;
    line-height: 32px;
    color: var(--white);
  }
</style>
</head>
<body>
<div class="cover">
  <svg class="facets" viewBox="0 0 848 1200" aria-hidden="true">
    <polygon points="0,0 848,0 848,290 770,150 600,95 420,72 240,100 110,160 0,300" fill="var(--blue-soft)"/>
    <polygon points="0,0 180,0 0,150" fill="var(--blue-deep)"/>
    <polygon points="0,150 180,0 110,160" fill="var(--blue-mid)"/>
    <polygon points="0,150 110,160 0,300" fill="var(--blue-dusk)"/>
    <polygon points="180,0 420,0 240,100" fill="var(--blue-mid)"/>
    <polygon points="240,100 420,0 420,72" fill="var(--blue-bright)"/>
    <polygon points="420,0 600,95 420,72" fill="var(--blue-deep)"/>
    <polygon points="420,0 640,0 600,95" fill="var(--blue-ice)"/>
    <polygon points="640,0 848,0 720,60" fill="var(--blue-mid)"/>
    <polygon points="600,95 640,0 770,150" fill="var(--blue-bright)"/>
    <polygon points="720,60 848,0 848,130" fill="var(--blue-soft)"/>
    <polygon points="770,150 720,60 848,130" fill="var(--blue-deep)"/>
    <polygon points="770,150 848,130 848,290" fill="var(--blue-ink)"/>
  </svg>

  <div class="portrait" role="img" aria-label="Photo of the father and son authors, shirtless, shaking hands and smiling, wearing board shorts"></div>

  <svg class="facets" viewBox="0 0 848 1200" aria-hidden="true">
    <polygon points="0,1005 690,1100 848,1200 0,1200" fill="var(--blue-mid)"/>
    <polygon points="0,1005 260,1041 0,1075" fill="var(--blue-bright)"/>
    <polygon points="690,1100 848,985 848,1200" fill="var(--blue-deep)"/>
    <polygon points="700,1030 848,985 760,1070" fill="var(--blue-soft)"/>
    <polygon points="690,1100 848,1080 848,1200" fill="var(--blue-ink)"/>
  </svg>

  <h1 class="title">Summit<br>Drive</h1>

  <p class="tagline">Push Past Your Limits, Find Strength Within Yourself</p>

  <p class="authors">Dale &amp; Owen Marsh</p>
  <p class="team">The Father and son fitness team</p>
</div>
</body>
</html>
```